North Carolina-themed postcard

Would like 3x distinct designs for a postcard (sized 4.5 x 5.5) that celebrates the state of North Carolina. A vintage theme, a modern theme, and a simple black/white theme would be suggestions for design styles.

```html
<!DOCTYPE html>
<html lang="en">
<head>
<meta charset="utf-8">
<title>Greetings from North Carolina – Postcard Front and Back</title>
<link rel="stylesheet" href="https://fonts.googleapis.com/css2?family=Satisfy&family=Luckiest+Guy&display=swap">
<style>
  :root {
    --navy-deep: #14306a;
    --navy: #23498f;
    --navy-light: #3f6db3;
    --leaf-green: #6cbf3a;
    --sky: #dfe9f6;
    --stone: #ece2c2;
    --lawn: #c3d69a;
    --cardinal-red: #e0303f;
    --edge-pink: #f08a90;
    --plum: #5a3f86;
    --paper: #ffffff;
    --mist: #ececec;
    --mist-dark: #d2d2d2;
    --ink-line: #333333;
    --stage: #d4d4d4;
  }
  * { margin: 0; padding: 0; box-sizing: border-box; }
  html, body {
    width: 1200px;
    height: 696px;
    overflow: hidden;
    background: var(--stage);
  }
  .stage {
    position: relative;
    width: 1200px;
    height: 696px;
    overflow: hidden;
    background: var(--stage);
  }
  .postcard {
    position: absolute;
    top: 161px;
    width: 560px;
    height: 374px;
    overflow: hidden;
    background: var(--paper);
    box-shadow: 0 6px 14px rgba(0, 0, 0, 0.28);
  }
  .postcard-back { left: 25px; }
  .postcard-front { left: 615px; }

  .capitol-backdrop-mono {
    position: absolute;
    inset: 0;
    background: linear-gradient(180deg, #f4f4f4 0%, var(--mist) 45%, var(--mist-dark) 80%, #c8c8c8 100%);
  }
  .capitol-backdrop {
    position: absolute;
    inset: 0;
    background: linear-gradient(180deg, var(--sky) 0%, #efe7cc 35%, var(--stone) 62%, #d9e2b6 82%, var(--lawn) 100%);
  }
  .card-art {
    position: absolute;
    inset: 0;
    width: 560px;
    height: 374px;
  }
  .greeting {
    font-family: "Satisfy", cursive;
  }
  .state-name {
    font-family: "Luckiest Guy", system-ui, sans-serif;
  }
</style>
</head>
<body>
<main class="stage">

  <section class="postcard postcard-back" aria-label="Postcard back">
    <div class="capitol-backdrop-mono" role="img" aria-label="Faint black and white photograph of the state capitol building with a statue"></div>
    <svg class="card-art" viewBox="0 0 600 400" aria-hidden="true">
      <line class="divider" x1="232" y1="28" x2="232" y2="372" stroke="var(--ink-line)" stroke-width="1.2"/>
      <rect class="stamp-box" x="468" y="30" width="104" height="74" fill="none" stroke="var(--ink-line)" stroke-width="1.5"/>
      <g class="address-lines" stroke="var(--ink-line)" stroke-width="1.2">
        <line x1="262" y1="168" x2="572" y2="168"/>
        <line x1="262" y1="216" x2="572" y2="216"/>
        <line x1="262" y1="264" x2="572" y2="264"/>
        <line x1="262" y1="312" x2="572" y2="312"/>
      </g>
    </svg>
  </section>

  <section class="postcard postcard-front" aria-label="Postcard front">
    <div class="capitol-backdrop" role="img" aria-label="Faded photograph of the state capitol building with its dome, columns, a statue and green lawn"></div>
    <svg class="card-art" viewBox="0 0 600 400">
      <defs>
        <linearGradient id="bandNavy" x1="0" y1="0" x2="0" y2="1">
          <stop offset="0" stop-color="var(--navy-deep)"/>
          <stop offset="0.6" stop-color="var(--navy)"/>
          <stop offset="1" stop-color="var(--navy-light)"/>
        </linearGradient>
        <linearGradient id="greetFill" x1="0" y1="1" x2="1" y2="0">
          <stop offset="0" stop-color="var(--navy-deep)"/>
          <stop offset="0.6" stop-color="var(--plum)"/>
          <stop offset="1" stop-color="var(--cardinal-red)"/>
        </linearGradient>
        <linearGradient id="emblemFill" x1="0" y1="0" x2="1" y2="1">
          <stop offset="0" stop-color="#f6f6f6"/>
          <stop offset="0.55" stop-color="#f3d6d6"/>
          <stop offset="1" stop-color="#e36a72"/>
        </linearGradient>
        <linearGradient id="letterFill" x1="0" y1="0" x2="0" y2="1">
          <stop offset="0" stop-color="#7fa9d8"/>
          <stop offset="0.5" stop-color="#6f8f5c"/>
          <stop offset="1" stop-color="#3f6b3a"/>
        </linearGradient>
        <path id="arcNorth" d="M118 370 Q240 300 338 196"/>
        <path id="arcCarolina" d="M232 392 Q420 330 590 182"/>
      </defs>

      <g class="top-band" aria-hidden="true">
        <path d="M0 0 H600 V20 C420 26 200 80 0 136 Z" fill="var(--leaf-green)"/>
        <path d="M0 0 H600 V10 C420 16 200 70 0 124 Z" fill="url(#bandNavy)"/>
      </g>
      <g class="bottom-band" aria-hidden="true">
        <rect x="0" y="386" width="600" height="5" fill="var(--leaf-green)"/>
        <rect x="0" y="391" width="600" height="9" fill="url(#bandNavy)"/>
      </g>

      <g class="state-emblem" role="img" aria-label="State bird cardinal with dogwood blossoms inside a hexagon badge">
        <polygon points="494,28 556,28 586,80 556,132 494,132 464,80" fill="#ffffff" stroke="#c9c9c9" stroke-width="1.5"/>
        <polygon points="499,37 551,37 576,80 551,123 499,123 474,80" fill="url(#emblemFill)"/>
      </g>

      <g class="greeting" transform="rotate(-27 110 200)">
        <text x="52" y="208" font-size="54" fill="url(#greetFill)" stroke="#ffffff" stroke-width="3" paint-order="stroke">Greetings</text>
        <text x="140" y="254" font-size="46" fill="var(--navy-deep)" stroke="#ffffff" stroke-width="3" paint-order="stroke">from</text>
      </g>

      <g class="state-name" role="img" aria-label="North Carolina, with letters filled by photographs of cities and mountains">
        <text font-size="54" fill="var(--edge-pink)" stroke="var(--cardinal-red)" stroke-width="1.5" transform="translate(2 6)"><textPath href="#arcNorth" textLength="250" lengthAdjust="spacingAndGlyphs">NORTH</textPath></text>
        <text font-size="54" fill="url(#letterFill)" stroke="#ffffff" stroke-width="3" paint-order="stroke"><textPath href="#arcNorth" textLength="250" lengthAdjust="spacingAndGlyphs">NORTH</textPath></text>
        <text font-size="54" fill="var(--edge-pink)" stroke="var(--cardinal-red)" stroke-width="1.5" transform="translate(2 6)"><textPath href="#arcCarolina" textLength="410" lengthAdjust="spacingAndGlyphs">CAROLINA</textPath></text>
        <text font-size="54" fill="url(#letterFill)" stroke="#ffffff" stroke-width="3" paint-order="stroke"><textPath href="#arcCarolina" textLength="410" lengthAdjust="spacingAndGlyphs">CAROLINA</textPath></text>
      </g>
    </svg>
  </section>

</main>
</body>
</html>
```